Amber Ridge,

Tri-fold brochure. This brochure is designed to get attention from college students who wish to get hands-on broadcast and online experience and do so covering interesting stories and people in places traditional media does not go. I'll be their professor and adviser. Would like the brochure as a single fold using 8.5 X 11 although I would appreciate any suggestions on size or number of folds.

I'm interested in a design the designer is interested in. Love passion. You can see I have this brochure generally mapped out, but I am not stuck on photo placement. I don't care if a photo stretches 2 or 3 pages. I'm interested in other design elements besides my photos and copy.

I've included several photos that can be used. The only photo I'm stuck on is the Marlow Pennick Building for the front page. It's a B&W page completely except for the Chicago flag at the bottom.

```html
<!DOCTYPE html>
<html lang="en">
<head>
<meta charset="utf-8">
<title>Small Town Amber Ridge – Brochure Spread</title>
<link rel="stylesheet" href="https://fonts.googleapis.com/css2?family=Roboto+Slab:wght@400;700&display=swap">
<style>
  :root {
    --backdrop: #e4e4e6;
    --charcoal: #1d1e21;
    --charcoal-soft: #2a2b2f;
    --brand-blue: #1672c4;
    --ring-blue: #5aa8ea;
    --ring-white: #f4f6f8;
    --ink-light: #ffffff;
    --ink-body: #e9ecef;
    --ink-dark: #1a1a1a;
  }
  * { box-sizing: border-box; margin: 0; padding: 0; }
  html, body { width: 1200px; height: 720px; overflow: hidden; background: var(--backdrop); }
  .canvas { position: relative; width: 1200px; height: 720px; }
  .spread {
    position: absolute; left: 60px; top: 10px; width: 1080px; height: 700px;
    display: flex; box-shadow: 0 6px 24px rgba(0,0,0,.25);
  }
  .page {
    position: relative; width: 540px; height: 700px; overflow: hidden;
    background: linear-gradient(135deg, var(--charcoal-soft), var(--charcoal) 60%);
    font-family: "Roboto Slab", serif;
  }
  .page svg.art { position: absolute; inset: 0; width: 540px; height: 700px; }
  .block { position: absolute; color: var(--ink-body); }
  .block h2 { font-size: 22px; font-weight: 700; color: var(--ink-light); margin-bottom: 8px; letter-spacing: .2px; }
  .block p { font-size: 11.5px; line-height: 1.3; margin-bottom: 6px; }
  .block.on-light { color: var(--ink-dark); }
  .block.on-light h2 { color: var(--ink-dark); }
  .intro { left: 48px; top: 56px; width: 290px; }
  .location { left: 250px; top: 320px; width: 230px; }
  .extra { left: 40px; top: 500px; width: 250px; }
  .social { left: 50px; top: 290px; width: 420px; }
</style>
</head>
<body>
<div class="canvas">
  <div class="spread">

    <section class="page page-left">
      <svg class="art" viewBox="0 0 540 700">
        <defs>
          <radialGradient id="muralTone"><stop offset="0" stop-color="#3e8f88"/><stop offset="1" stop-color="#6b4a34"/></radialGradient>
          <radialGradient id="stationTone"><stop offset="0" stop-color="#b04b52"/><stop offset="1" stop-color="#2d3447"/></radialGradient>
          <radialGradient id="foodTone"><stop offset="0" stop-color="#c9502e"/><stop offset="1" stop-color="#d8c89a"/></radialGradient>
        </defs>
        <polygon class="accent-band" points="160,295 540,255 540,565 300,480" fill="var(--brand-blue)"/>
        <g role="img" aria-label="Circular photo of a colourful street mural">
          <circle cx="440" cy="150" r="104" fill="var(--ring-blue)"/>
          <circle cx="440" cy="150" r="100" fill="var(--ring-white)"/>
          <circle cx="440" cy="150" r="96" fill="url(#muralTone)"/>
        </g>
        <g role="img" aria-label="Circular photo of commuters crowding a train station platform">
          <circle cx="105" cy="330" r="104" fill="var(--ring-blue)"/>
          <circle cx="105" cy="330" r="100" fill="var(--ring-white)"/>
          <circle cx="105" cy="330" r="96" fill="url(#stationTone)"/>
        </g>
        <g role="img" aria-label="Circular photo of a loaded hot dog with pickle and tomato">
          <circle cx="470" cy="620" r="88" fill="var(--ring-blue)"/>
          <circle cx="470" cy="620" r="84" fill="var(--ring-white)"/>
          <circle cx="470" cy="620" r="80" fill="url(#foodTone)"/>
        </g>
      </svg>

      <div class="block intro">
        <h2>Small Town Amber Ridge</h2>
        <p>Spend the time necessary to consider your business requirements, your needs and your budget yield to your IT services expectations, not what we think you should have.</p>
        <p>Prevent potential down time and data loss disasters from occurring instead of reactively dousing the fire with our computer support</p>
      </div>
      <div class="block location">
        <h2>Tapped on location</h2>
        <p>Spend the time necessary to consider your business requirements, your needs and your budget yield to your IT services expectations, not what we think you should have.</p>
        <p>Prevent potential down time and data loss disasters from occurring instead of reactively dousing the fire with our computer support</p>
      </div>
      <div class="block extra">
        <h2>Some Copy here</h2>
        <p>Spend the time necessary to consider your business requirements, your needs and your budget yield to your IT services expectations, not what we think you should have.</p>
      </div>
    </section>

    <section class="page page-right">
      <svg class="art" viewBox="0 0 540 700">
        <defs>
          <linearGradient id="crowdTone" x1="0" y1="0" x2="1" y2="1"><stop offset="0" stop-color="#2f8ee0"/><stop offset="1" stop-color="#0f5ea8"/></linearGradient>
          <linearGradient id="skylineTone" x1="0" y1="0" x2="0" y2="1"><stop offset="0" stop-color="#8d8f92"/><stop offset="1" stop-color="#d6d7d8"/></linearGradient>
          <radialGradient id="musicianTone"><stop offset="0" stop-color="#3a2a22"/><stop offset="1" stop-color="#9c6a4a"/></radialGradient>
          <radialGradient id="fountainTone"><stop offset="0" stop-color="#b86a5c"/><stop offset="1" stop-color="#4f6e86"/></radialGradient>
        </defs>
        <polygon role="img" aria-label="Blue-toned photo of people walking on a city street" points="0,0 540,0 540,200 0,270" fill="url(#crowdTone)"/>
        <polygon role="img" aria-label="Black and white photo of the Marlow Pennick Building rising above fog" points="0,400 360,700 0,700" fill="url(#skylineTone)"/>
        <g role="img" aria-label="Circular photo of a street musician playing trumpet">
          <circle cx="455" cy="170" r="100" fill="var(--ring-blue)"/>
          <circle cx="455" cy="170" r="96" fill="var(--ring-white)"/>
          <circle cx="455" cy="170" r="92" fill="url(#musicianTone)"/>
        </g>
        <g role="img" aria-label="Circular photo of children playing in a fountain">
          <circle cx="410" cy="590" r="114" fill="var(--ring-blue)"/>
          <circle cx="410" cy="590" r="110" fill="var(--ring-white)"/>
          <circle cx="410" cy="590" r="106" fill="url(#fountainTone)"/>
        </g>
      </svg>

      <div class="block social">
        <h2>Social Media</h2>
        <p>Spend the time necessary to consider your business requirements, your needs and your budget yield to your IT services expectations, not what we think you should have.</p>
        <p>Prevent potential down time and data loss disasters from occurring instead of reactively dousing the fire with our computer support</p>
      </div>
    </section>

  </div>
</div>
</body>
</html>
```